Foldable Quorvane Headphone Packaging Design

We would like a window box style packaging design for our Foldable Quorvane Headphone.

We want to use the packaging for 4-5 of our Quorvane headphone series (enclosed picture of the headphones for reference) and hence we would not like to put any product pictures on the packaging.
Material: E-Flute Paper box
Type: Window Box style
Design features we prefer: Colorful, creative, trendy, High tech.
Requirement: AI file is preferred
Size of Packaging: 170 (L) x 120 (W) x 200 (H) mm

Enclosed are a detailed description along with competitor designs for your reference.

Any further questions, please feel free to ask.

Target Market(s)

25-35 year olds

Industry/Entity Type

Electronics

Colors

Designer to choose colors to be used in the design.

Requirements
Must have
• Trendy Design

```html
<!DOCTYPE html>
<html lang="en">
<head>
<meta charset="utf-8">
<title>Foldable Quorvane Headphone – Window Box Dieline</title>
<link href="https://fonts.googleapis.com/css2?family=Quicksand:wght@300;400;500&family=Orbitron:wght@500;700&family=Open+Sans:wght@400;600;700&display=swap" rel="stylesheet">
<style>
  :root {
    --ink: #0b1f24;
    --teal: #17b5bb;
    --teal-deep: #137c80;
    --paper: #ffffff;
    --stage: #f3f5f6;
    --line: #2b4a50;
  }
  html, body {
    margin: 0;
    width: 1200px;
    height: 1200px;
    overflow: hidden;
    background: var(--stage);
  }
  .dieline {
    position: absolute;
    left: 0;
    top: 206px;
    width: 1200px;
    height: 788px;
  }
  .panel { fill: var(--ink); }
  .band { fill: var(--teal); }
  .tag { fill: var(--teal-deep); }
  .window { fill: var(--paper); stroke: var(--teal); stroke-width: 3; }
  .bracket { fill: none; stroke: #c9d6d8; stroke-width: 1.2; }
  .brand-company { font-family: 'Quicksand', sans-serif; font-weight: 400; fill: var(--teal); }
  .brand-name { font-family: 'Quicksand', sans-serif; font-weight: 400; fill: #ffffff; }
  .title-small { font-family: 'Quicksand', sans-serif; font-weight: 400; fill: var(--ink); }
  .title-large { font-family: 'Quicksand', sans-serif; font-weight: 400; fill: var(--ink); }
  .feature-head { font-family: 'Orbitron', sans-serif; font-weight: 500; fill: #ffffff; font-size: 8px; letter-spacing: .5px; }
  .feature-item { font-family: 'Orbitron', sans-serif; font-weight: 500; fill: #ffffff; font-size: 6px; letter-spacing: .4px; }
  .maker { font-family: 'Open Sans', sans-serif; font-weight: 700; fill: #ffffff; font-size: 15px; }
  .spec-head { font-family: 'Open Sans', sans-serif; font-weight: 700; fill: #ffffff; font-size: 7.5px; }
  .spec-label { font-family: 'Open Sans', sans-serif; font-weight: 400; fill: #ffffff; font-size: 5.6px; }
  .spec-value { font-family: 'Open Sans', sans-serif; font-weight: 700; fill: #ffffff; font-size: 5.6px; }
  .body-copy { font-family: 'Open Sans', sans-serif; font-weight: 400; fill: #ffffff; font-size: 5.2px; }
  .fine-print { font-family: 'Open Sans', sans-serif; font-weight: 400; fill: #ffffff; font-size: 4.4px; }
  .cert { fill: none; stroke: #ffffff; stroke-width: 1.4; }
  .cert-solid { fill: #ffffff; }
</style>
</head>
<body>
<svg class="dieline" viewBox="215 730 1125 739" xmlns="http://www.w3.org/2000/svg" aria-label="Flat dieline of the Foldable Quorvane Headphone window box">
  <defs>
    <linearGradient id="product-fade" x1="0" y1="0" x2="1" y2="1">
      <stop offset="0" stop-color="#16363c"/>
      <stop offset="1" stop-color="#0f2a2f"/>
    </linearGradient>
  </defs>

  <!-- Left side panel with top and bottom flaps -->
  <g class="side-left">
    <polygon class="panel" points="225,945 255,835 435,835 445,945"/>
    <path class="panel" d="M225,945 H445 V1315 L330,1395 V1450 Q330,1455 325,1455 H230 Q225,1455 225,1450 Z"/>
    <rect class="band" x="291" y="983" width="89" height="294"/>
    <g transform="translate(336,1130) rotate(-90)">
      <text class="title-small" x="0" y="-2" font-size="25" text-anchor="middle">Foldable Quorvane</text>
      <text class="title-large" x="0" y="30" font-size="46" text-anchor="middle">Headphone</text>
    </g>
  </g>

  <!-- Front panel with tuck lid and bottom flap -->
  <g class="front">
    <path class="panel" d="M448,945 V752 Q448,740 460,740 H745 Q757,740 757,752 V945 Z"/>
    <path class="panel" d="M445,945 H760 V1455 H690 V1415 H515 V1455 H445 Z"/>

    <g class="lid-brand">
      <path class="bracket" d="M556,808 V801 H563 M642,801 H649 V808 M556,838 V845 H563 M642,845 H649 V838"/>
      <text class="brand-company" x="602" y="819" font-size="15" text-anchor="middle">Company</text>
      <text class="brand-name" x="602" y="837" font-size="13" text-anchor="middle">Name</text>
      <rect class="band" x="446" y="862" width="314" height="54"/>
      <text class="title-small" x="603" y="884" font-size="16" text-anchor="middle">Foldable Quorvane</text>
      <text class="title-large" x="603" y="907" font-size="26" text-anchor="middle">Headphone</text>
    </g>

    <g class="front-brand">
      <path class="bracket" d="M492,982 V975 H499 M578,975 H585 V982 M492,1011 V1018 H499 M578,1018 H585 V1011"/>
      <text class="brand-company" x="538" y="993" font-size="15" text-anchor="middle">Company</text>
      <text class="brand-name" x="538" y="1011" font-size="13" text-anchor="middle">Name</text>
      <rect class="band" x="445" y="1035" width="187" height="55"/>
      <text class="title-small" x="539" y="1058" font-size="15.5" text-anchor="middle">Foldable Quorvane</text>
      <text class="title-large" x="539" y="1081" font-size="26" text-anchor="middle">Headphone</text>
    </g>

    <g role="img" aria-label="Faint line illustration of folded headphones">
      <rect x="452" y="1100" width="170" height="105" rx="40" fill="url(#product-fade)" opacity="0.7"/>
    </g>

    <g class="features">
      <polygon class="tag" points="446,1212 519,1212 511,1226 446,1226"/>
      <text class="feature-head" x="453" y="1222">FEATURES</text>
      <g class="feature-item">
        <circle cx="457" cy="1239" r="1" fill="#fff"/><text x="466" y="1241">WIRELESS VERSION 5.0</text>
        <circle cx="457" cy="1251" r="1" fill="#fff"/><text x="466" y="1253">FOLDABLE AND PORTABLE</text>
        <circle cx="457" cy="1263" r="1" fill="#fff"/><text x="466" y="1265">EXCEPTIONAL SOUND QUALITY</text>
        <circle cx="457" cy="1275" r="1" fill="#fff"/><text x="466" y="1277">DUAL MODE WIRELESS OR</text>
        <text x="466" y="1286">WIRED CONNECTIVITY</text>
        <circle cx="457" cy="1296" r="1" fill="#fff"/><text x="466" y="1298">ADJUSTABLE HEADBAND</text>
      </g>
    </g>

    <g class="maker-mark">
      <text class="maker" transform="translate(613,1282) rotate(-90)">Quorvane</text>
      <circle cx="607" cy="1293" r="7" fill="var(--teal)"/>
    </g>
  </g>

  <!-- Right side panel with flaps -->
  <g class="side-right">
    <polygon class="panel" points="760,945 770,835 950,835 980,945"/>
    <path class="panel" d="M760,945 H980 V1315 L980,1395 L878,1395 V1450 Q878,1455 873,1455 H765 Q760,1455 760,1450 Z"/>
  </g>

  <!-- Back panel with glue tab and bottom flap -->
  <g class="back">
    <path class="panel" d="M1102,945 V880 Q1102,872 1110,872 H1164 Q1172,872 1172,880 V945 Z"/>
    <path class="panel" d="M980,945 H1295 L1330,958 V1305 L1220,1410 V1450 Q1220,1455 1215,1455 H1060 Q1055,1455 1055,1450 V1410 L980,1315 Z"/>

    <g class="spec">
      <polygon class="tag" points="1110,963 1184,963 1176,977 1110,977"/>
      <text class="spec-head" x="1116" y="973">Specification</text>
      <g>
        <text class="spec-label" x="1122" y="992">Wireless Version</text><text class="spec-value" x="1203" y="992">: 5.0</text>
        <text class="spec-label" x="1122" y="1002">Wireless Playback Duration</text><text class="spec-value" x="1203" y="1002">: 10-12 h</text>
        <text class="spec-label" x="1122" y="1012">Standby Time</text><text class="spec-value" x="1203" y="1012">: 80 h</text>
        <text class="spec-label" x="1122" y="1022">Wireless Range</text><text class="spec-value" x="1203" y="1022">: 10 m</text>
        <text class="spec-label" x="1122" y="1032">Impedance</text><text class="spec-value" x="1203" y="1032">: 32 Ω</text>
        <text class="spec-label" x="1122" y="1042">Sound Pressure Level</text><text class="spec-value" x="1203" y="1042">: 100dB ± 3dB</text>
        <text class="spec-label" x="1122" y="1052">Frequency Response</text><text class="spec-value" x="1203" y="1052">: 20 - 20kHz</text>
        <text class="spec-label" x="1122" y="1062">Plug Type</text><text class="spec-value" x="1203" y="1062">: 3.5mm Stereo Detachable</text>
        <text class="spec-label" x="1122" y="1072">Driver Unit</text><text class="spec-value" x="1203" y="1072">: 40mm</text>
      </g>

      <polygon class="tag" points="1110,1081 1155,1081 1149,1090 1110,1090"/>
      <text class="spec-label" x="1115" y="1088" font-weight="700">Warning</text>
      <text class="body-copy" x="1122" y="1099">Lorem ipsum dolor sit amet, consectetur adipiscing elit.</text>
      <text class="body-copy" x="1122" y="1107">Curabitur dapibus vitae mauris consectetur fermentum.</text>
      <text class="body-copy" x="1122" y="1115">Pellentesque eleifend vel orci non tristique.</text>

      <polygon class="tag" points="1110,1124 1155,1124 1149,1133 1110,1133"/>
      <text class="spec-label" x="1115" y="1131" font-weight="700">Cautions</text>
      <text class="body-copy" x="1122" y="1142">Lorem ipsum dolor sit amet, consectetur adipiscing elit.</text>
      <text class="body-copy" x="1122" y="1150">Curabitur dapibus vitae mauris consectetur fermentum.</text>
      <text class="body-copy" x="1122" y="1158">Pellentesque eleifend vel orci non tristique.</text>

      <path class="bracket" d="M1127,1175 V1169 H1132 M1270,1169 H1275 V1175 M1127,1225 V1231 H1132 M1270,1231 H1275 V1225"/>

      <text class="fine-print" x="1122" y="1248">© 2019 Lorem ipsum dolor sit amet,</text>
      <text class="fine-print" x="1122" y="1255">consectetur adipiscing elit. Curabitur dapibus vitae mauris consec</text>
      <text class="fine-print" x="1122" y="1262">tetur fermentum. Pellentesque eleifend vel orci non tristique. Donec</text>
      <text class="fine-print" x="1122" y="1269">a orci luctus, bibendum leo a, hendrerit nunc. Proin tristique ut.</text>

      <g class="cert-row">
        <rect class="cert" x="1122" y="1286" width="16" height="14" rx="2"/>
        <circle class="cert" cx="1154" cy="1293" r="7"/>
        <polygon class="cert" points="1186,1285 1195,1300 1177,1300"/>
        <circle class="cert" cx="1210" cy="1293" r="6.5"/>
        <rect class="cert" x="1226" y="1286" width="9" height="14"/>
        <polygon class="cert" points="1252,1286 1259,1299 1245,1299"/>
        <circle class="cert-solid" cx="1272" cy="1293" r="7"/>
      </g>
    </g>
  </g>

  <!-- Die-cut window spanning front, side and back -->
  <rect class="window" x="632" y="947" width="476" height="366" rx="14"/>
</svg>
</body>
</html>
```